Broadcaster,Conference Host,Facilitator

Looking for a business card and logo to create the Grant Ollerby brand .. Something with a slant towards radio and conference speaking
I like the idea of classic black white or grey but open to suggestions

Target Market(s)

Corporates

Industry/Entity Type

Business

Contact Information for Business Card

Grant Ollerby
Email : Grant.Ollerby@fenmail.co.uk
Mobile : +44 7700 900216
Social : @Grantollerby

Font styles to use
Serif
Decorative
Script

Requirements
Must have
• Feel classy and dynamic
Should not have
• Cartoons

```html
<!DOCTYPE html>
<html lang="en">
<head>
<meta charset="utf-8">
<title>Grant Ollerby — Business Card</title>
<link rel="stylesheet" href="https://fonts.googleapis.com/css2?family=Josefin+Sans:wght@400&family=PT+Sans:wght@400&display=swap">
<style>
  :root {
    --backdrop: #e4e4e2;
    --card: #ffffff;
    --band: #7a7a7a;
    --ink: #4a4a4a;
    --ink-light: #f4f4f4;
    --mic-dark: #262626;
    --mic-mid: #555555;
  }
  * { margin: 0; padding: 0; box-sizing: border-box; }
  html, body {
    width: 1200px;
    height: 873px;
    overflow: hidden;
    background: var(--backdrop);
  }
  .canvas {
    position: relative;
    width: 1200px;
    height: 873px;
    display: flex;
    align-items: center;
    justify-content: center;
    gap: 48px;
  }
  .card {
    position: relative;
    width: 520px;
    height: 320px;
    background: var(--card);
    box-shadow: 0 2px 10px rgba(0,0,0,0.12);
    overflow: hidden;
  }

  /* Back side: contact details */
  .card-back .band {
    position: absolute;
    left: 0;
    right: 0;
    top: 70px;
    height: 60px;
    background: var(--band);
  }
  .contact-list {
    position: absolute;
    left: 150px;
    top: 152px;
    list-style: none;
    font-family: "PT Sans", sans-serif;
    font-size: 16px;
    line-height: 22px;
    color: var(--ink);
    white-space: nowrap;
  }

  /* Front side: mark and name */
  .card-front .accent-square {
    position: absolute;
    left: 0;
    top: 96px;
    width: 48px;
    height: 66px;
    background: var(--band);
  }
  .card-front .mic-art {
    position: absolute;
    left: 58px;
    top: 34px;
    width: 150px;
    height: 210px;
    border-radius: 60px 60px 14px 14px;
    background: linear-gradient(160deg, var(--mic-mid), var(--mic-dark));
  }
  .card-front .name-band {
    position: absolute;
    left: 212px;
    right: 0;
    top: 192px;
    height: 56px;
    background: var(--band);
    display: flex;
    align-items: center;
    justify-content: flex-end;
    padding-right: 26px;
  }
  .name {
    font-family: "Josefin Sans", sans-serif;
    font-variant: small-caps;
    font-size: 30px;
    letter-spacing: 1px;
    color: var(--ink-light);
    font-weight: 400;
    white-space: nowrap;
  }
</style>
</head>
<body>
  <main class="canvas">
    <section class="card card-back" aria-label="Business card back">
      <div class="band"></div>
      <ul class="contact-list">
        <li>Email : Grant.Ollerby@fenmail.co.uk</li>
        <li>Mobile : +44 7700 900216</li>
        <li>Social : @Grantollerby</li>
      </ul>
    </section>

    <section class="card card-front" aria-label="Business card front">
      <div class="accent-square"></div>
      <div class="mic-art" role="img" aria-label="Illustration of a vintage studio microphone in black ink"></div>
      <div class="name-band">
        <span class="name">GrantOllerby</span>
      </div>
    </section>
  </main>
</body>
</html>
```